Natural Sunscreen Label Design for a Natural Cosmetics brand

We are looking to create a label design for a Natural Sunscreen Lotion. The labels will be a stick-on label on a white background tube. Enclosed a file with the content and some ideas/references. Please feel free to explore more.

It is important that the SPF is highlighted as large text and to use colors that give the customer an impression this being a sunscreen from far away as well.
We like white and orange/amber/yellow.
Details attached
Our Logo is attached as well as the size template of the label.

```html
<!DOCTYPE html>
<html lang="en">
<head>
<meta charset="utf-8">
<title>Natural Sun Lotion – SPF 30+ Label</title>
<link rel="stylesheet" href="https://fonts.googleapis.com/css2?family=Crimson+Text:ital,wght@0,400;0,700;1,700&family=Great+Vibes&family=Raleway:wght@300;400;700&family=Tinos:wght@700&family=Ubuntu:wght@400;500;700&display=swap">
<style>
  :root {
    --white: #ffffff;
    --orange: #ff9800;
    --flame: #fa4616;
    --ink: #1e1e1e;
    --heading: #33271a;
    --cream: #fff3dc;
    --leaf: #2e7d1f;
  }
  * { margin: 0; padding: 0; box-sizing: border-box; }
  html, body { width: 1200px; height: 1110px; overflow: hidden; background: var(--white); }
  .label { position: relative; width: 1200px; height: 1110px; background: var(--white); font-family: "Crimson Text", serif; }

  /* Front panel */
  .front { position: absolute; left: 0; top: 0; width: 601px; height: 1110px; }
  .brand-mark { position: absolute; left: 224px; top: 87px; width: 152px; height: 152px; border-radius: 50%; background: var(--flame); display: flex; align-items: center; justify-content: center; }
  .brand-mark span { font-family: "Ubuntu", sans-serif; font-weight: 500; font-size: 19px; letter-spacing: 2px; color: var(--white); }
  .line-name { position: absolute; left: 0; width: 601px; top: 252px; text-align: center; font-family: "Great Vibes", cursive; font-size: 42px; line-height: 1.2; color: var(--ink); }
  .product-title { position: absolute; left: 0; width: 601px; top: 296px; text-align: center; font-family: "Ubuntu", sans-serif; font-weight: 700; font-size: 89px; line-height: 1; color: var(--flame); letter-spacing: -1px; }
  .product-type { position: absolute; left: 0; width: 601px; top: 376px; text-align: center; font-family: "Ubuntu", sans-serif; font-weight: 400; font-size: 66px; line-height: 1; color: var(--ink); }
  .sun-art { position: absolute; left: 222px; top: 484px; width: 156px; height: 214px; border-radius: 50%; background: radial-gradient(circle at 50% 45%, var(--orange) 55%, rgba(255,152,0,0.75) 100%); }
  .spf-band { position: absolute; left: 0; top: 563px; width: 601px; height: 121px; background: var(--orange); }
  .spf-value { position: absolute; left: 0; width: 601px; top: 572px; text-align: center; font-family: "Tinos", serif; font-weight: 700; font-size: 98px; line-height: 1; color: var(--white); }
  .protection { position: absolute; left: 0; width: 601px; top: 738px; text-align: center; font-family: "Raleway", sans-serif; font-weight: 300; font-size: 51px; line-height: 1; color: var(--ink); }
  .usage { position: absolute; left: 0; width: 601px; top: 789px; text-align: center; font-family: "Raleway", sans-serif; font-weight: 700; font-size: 22px; color: var(--flame); }
  .benefits { position: absolute; left: 0; top: 882px; list-style: none; }
  .benefits li { position: relative; height: 29px; padding-left: 90px; font-family: "Raleway", sans-serif; font-size: 20.5px; line-height: 29px; color: var(--ink); }
  .benefits li::before { content: ""; position: absolute; left: 0; top: 6px; width: 76px; height: 18px; background: linear-gradient(90deg, var(--flame), rgba(250,70,22,0)); }
  .vegan-badge { position: absolute; left: 451px; top: 934px; }

  /* Back panel */
  .back { position: absolute; left: 601px; top: 0; width: 599px; height: 1110px; background: var(--orange); color: var(--white); }
  .intro { position: absolute; left: 29px; top: 36px; width: 540px; font-style: italic; font-weight: 700; font-size: 21px; line-height: 25.5px; }
  .features { position: absolute; left: 28px; top: 160px; width: 548px; font-size: 21px; line-height: 25.4px; }
  .features b, .ingredients b { color: var(--heading); font-weight: 700; }
  .section-bar { position: absolute; left: 32px; width: 543px; height: 35px; background: linear-gradient(90deg, var(--cream), rgba(255,243,220,0.5) 55%, rgba(255,152,0,0.6)); color: var(--heading); font-weight: 400; font-size: 25px; line-height: 35px; padding-left: 7px; }
  .bar-ingredients { top: 448px; }
  .bar-warnings { top: 706px; }
  .ingredients { position: absolute; left: 33px; top: 498px; width: 565px; font-size: 21px; line-height: 28.3px; }
  .warnings { position: absolute; left: 33px; top: 750px; width: 540px; font-size: 21px; line-height: 25.4px; color: var(--heading); }
  .warnings p.cont { padding-left: 6px; }
  .maker { position: absolute; left: 42px; top: 923px; font-size: 21px; line-height: 25.4px; color: var(--white); font-style: normal; }
  .volume { position: absolute; left: 345px; top: 924px; font-family: "Ubuntu", sans-serif; font-size: 37px; line-height: 1; color: var(--white); }
  .volume .estimate { font-style: italic; font-weight: 700; }
  .barcode-box { position: absolute; left: 333px; top: 975px; width: 190px; height: 63px; border: 2px solid var(--white); display: flex; align-items: center; justify-content: center; font-size: 21px; color: var(--white); }
</style>
</head>
<body>
<main class="label">
  <section class="front">
    <div class="brand-mark"><span>SOLMARINA</span></div>
    <p class="line-name">Brisamar</p>
    <h1 class="product-title">Natural Sun</h1>
    <p class="product-type">Lotion</p>

    <div class="sun-art" role="img" aria-label="Rising sun illustration with rays"></div>
    <div class="spf-band"></div>
    <p class="spf-value">SPF 30+</p>

    <p class="protection">UVA+UVB</p>
    <p class="usage">FOR BODY AND FACE</p>

    <ul class="benefits">
      <li>Non-Greasy</li>
      <li>BIO Aloe Vera</li>
      <li>Water Resistant</li>
      <li>Safe for Kids and Adults</li>
    </ul>

    <svg class="vegan-badge" width="106" height="60" viewBox="0 0 106 60" role="img" aria-label="Vegan certification badge">
      <ellipse cx="53" cy="30" rx="50" ry="26" fill="var(--leaf)"/>
    </svg>
  </section>

  <section class="back">
    <p class="intro">Experience the beauty of sunrise with Dawnleaf Botanics, our natural sun lotion designed to embrace the wonders of nature and keep your skin protected and radiant throughout the day.</p>

    <div class="features">
      <p><b>Sunshine Shield Technology:</b> Utilizes natural minerals and antioxidants to form a protective barrier against harmful UV rays, helping to prevent sunburn and skin damage.</p>
      <p><b>Eco-Friendly Formula:</b> Crafted with biodegradable ingredients that are gentle on both your skin and the environment, ensuring a guilt-free sunbathing experience.</p>
      <p><b>Hydra-Lock Moisture Infusion:</b> Infused with nourishing botanicals and hydrating extracts, this lotion locks in moisture to keep your skin soft and supple under the sun's</p>
    </div>

    <h2 class="section-bar bar-ingredients">INGREDIENTS</h2>
    <div class="ingredients">
      <p><b>Aloe Vera Gel:</b> Soothes and hydrates the skin, helping to alleviate sunburn and irritation.</p>
      <p><b>Coconut Oil:</b> Provides natural moisturization and forms a protective barrier on the skin.</p>
      <p><b>Green Tea Extract:</b> Rich in antioxidants, it helps to neutralize free radicals and protect the skin from sun damage.</p>
    </div>

    <h2 class="section-bar bar-warnings">WARNINGS:</h2>
    <div class="warnings">
      <p>"For external use only. Avoid contact with eyes.</p>
      <p class="cont">If contact occurs, rinse thoroughly with water."</p>
      <p>"Do not apply to damaged or broken skin."</p>
      <p>"Discontinue use if irritation or rash occurs.</p>
      <p class="cont">Consult a physician if irritation persists."</p>
    </div>

    <address class="maker">Helio Leaf Naturals<br>48 Amberlight Avenue<br>Goldfield, CA 90412<br>United States</address>
    <p class="volume">100ml <span class="estimate">e</span></p>
    <div class="barcode-box">BARCODE</div>
  </section>
</main>
</body>
</html>
```